Marlow Naturopathics business card design

Using the marlow logo designed, we would like that incorporated into a business card. A colour scheme which works with the logo and lists the following business details:

Dennis Marlow - Naturopath
Suite 4, 58 Torvane Street
Harbourton NSW
(02) 4391 7084
www.dennismarlowhealth-example.com

We would also like space on the back of the card for next appointment times.

Target Market(s)

Anyone looking to improve their health

Industry/Entity Type

Business

Requirements
Must have
• Marlow Naturopathics logo, business details.
Nice to have
• Good colour schemes, attractive, eye-catching features that are easy to read.

```html
<!DOCTYPE html>
<html lang="en">
<head>
<meta charset="utf-8">
<title>Marlow Naturopathics – Business Card</title>
<link href="https://fonts.googleapis.com/css2?family=Cinzel:wght@400;600;700&display=swap" rel="stylesheet">
<style>
  :root {
    --page: #ece9e4;
    --card: #ffffff;
    --navy: #0f3560;
    --brand-blue: #2a5f9e;
    --sky: #2e9bd6;
    --ink: #1b1b1b;
    --caption: #3a8fc9;
    --sunday: #d42a2a;
    --box-line: #2f6aa5;
  }
  * { box-sizing: border-box; margin: 0; padding: 0; }
  html, body { width: 1200px; height: 867px; overflow: hidden; }
  body {
    background: var(--page);
    font-family: "Cinzel", serif;
    color: var(--ink);
    position: relative;
  }
  .card {
    position: absolute;
    width: 560px;
    height: 340px;
    background: var(--card);
    border-radius: 16px;
    box-shadow: 0 6px 18px rgba(0,0,0,0.18);
    overflow: hidden;
  }

  /* Back: appointment card */
  .card-back { left: 60px; top: 60px; }
  .field { position: absolute; text-align: center; }
  .field .rule { border-bottom: 2px dotted var(--navy); height: 1px; }
  .field .label {
    font-size: 11px; color: var(--caption); letter-spacing: 1px; margin-top: 4px;
  }
  .field-name { left: 90px; top: 46px; width: 400px; }
  .appointment-heading {
    position: absolute; left: 0; right: 0; top: 92px; text-align: center;
    font-size: 14px; color: var(--navy); letter-spacing: 0.5px;
  }
  .days { position: absolute; left: 150px; top: 122px; display: flex; gap: 8px; }
  .day { width: 26px; text-align: center; }
  .box {
    width: 22px; height: 20px; margin: 0 auto;
    border: 1.5px solid var(--box-line); border-radius: 5px;
  }
  .day-letter { display: block; font-size: 11px; margin-top: 4px; color: var(--navy); }
  .day.sunday .day-letter { color: var(--sunday); }
  .field-date { left: 62px; top: 208px; width: 170px; }
  .at-word { position: absolute; left: 256px; top: 196px; font-size: 11px; color: var(--navy); }
  .field-time { left: 298px; top: 208px; width: 130px; }
  .meridiem { position: absolute; left: 446px; top: 186px; display: flex; gap: 8px; }
  .web-band {
    position: absolute; left: 0; right: 0; bottom: 0; height: 36px;
    background: var(--navy); color: #ffffff;
    font-size: 13px; font-weight: 600; letter-spacing: 1px;
    display: flex; align-items: center; justify-content: center;
  }

  /* Front: identity card */
  .card-front { left: 580px; top: 460px; }
  .brand-name {
    position: absolute; left: 44px; top: 62px; width: 250px;
    font-size: 24px; font-weight: 700; color: var(--brand-blue);
    line-height: 1.1; letter-spacing: 1px;
  }
  .brand-mark {
    position: absolute; right: 30px; top: 56px;
    width: 200px; height: 200px; border-radius: 50%;
    background: radial-gradient(circle at 45% 40%, #5fb6e6, #1f6fb8);
  }
  .person { position: absolute; left: 44px; top: 168px; }
  .person-name { font-size: 22px; font-weight: 600; color: var(--ink); letter-spacing: 0.5px; }
  .person-role { font-size: 14px; color: var(--sky); margin-top: 2px; letter-spacing: 0.5px; }
  .contact {
    position: absolute; left: 44px; top: 240px;
    font-size: 13px; line-height: 1.3; color: var(--ink); font-style: normal;
  }
</style>
</head>
<body>

  <section class="card card-back" aria-label="Appointment card">
    <div class="field field-name"><div class="rule"></div><div class="label">Name</div></div>
    <p class="appointment-heading">Has an appointment on</p>
    <div class="days">
      <div class="day"><div class="box"></div><span class="day-letter">M</span></div>
      <div class="day"><div class="box"></div><span class="day-letter">T</span></div>
      <div class="day"><div class="box"></div><span class="day-letter">W</span></div>
      <div class="day"><div class="box"></div><span class="day-letter">T</span></div>
      <div class="day"><div class="box"></div><span class="day-letter">F</span></div>
      <div class="day"><div class="box"></div><span class="day-letter">S</span></div>
      <div class="day sunday"><div class="box"></div><span class="day-letter">S</span></div>
    </div>
    <div class="field field-date"><div class="rule"></div><div class="label">Date</div></div>
    <span class="at-word">at</span>
    <div class="field field-time"><div class="rule"></div><div class="label">Time</div></div>
    <div class="meridiem">
      <div class="day"><div class="box"></div><span class="day-letter">AM</span></div>
      <div class="day"><div class="box"></div><span class="day-letter">PM</span></div>
    </div>
    <div class="web-band">www.dennismarlowhealth-example.com</div>
  </section>

  <section class="card card-front" aria-label="Business card">
    <p class="brand-name">Marlow<br>Naturopathics</p>
    <div class="brand-mark" role="img" aria-label="Marlow Naturopathics brand symbol"></div>
    <div class="person">
      <p class="person-name">Dennis Marlow</p>
      <p class="person-role">Naturopath</p>
    </div>
    <address class="contact">
      Suite 4<br>
      58 Torvane Street<br>
      Harbourton NSW<br>
      (02) 4391 7084
    </address>
  </section>

</body>
</html>
```